Webdesign für Wandertouren
Hi Wenke, thank you very much for the wonderful and successful collaboration. I was very pleased that you contributed your ideas so well. I'm really happy with your design and I'm looking forward to the reactions of my guests. I wish you many great clients and a lot of success in the future. Best regards Rieke
Zielgruppe
Liebe Designende, wunderbar, dass Du hier gelandet bist.
Ich biete als International Mountain Leader
Wandertouren, Trekkingreisen und Naturerlebnisse - regional und international an. Die Touren werden (noch alle) von mir persönlich durchgeführt.
Hier der Einstiegstext für die Startseite.
Atemberaubende Landschaften mit majestätischen Bergen, wunderschönen Hochebenen und beeindruckenden Wasserfällen verzaubern Deine Seele.
Wandertouren, Trekkingreisen und Naturerlebnisse führen Dich in fantastische Paradieswelten. Hier erlebst Du eindrucksvolle Glücksgefühle. Gerührt von der Schönheit und der Einzigartigkeit der wundervollen Natur kannst Du Dich tief entspannen und die Gegenwart genießen.
On Top gibt es dazu urige Berghütten und inspirierende Begegnungen, die Deine Bergabenteuer zu wundervollen Erlebnissen für Dich machen.
Und hast Du schon Lust bekommen mitzukommen?
Zielgruppe: Frauen und Männer zwischen 38 - 65 Jahren
Aufgabenstellung
*Ich liebe den Hintergrund mit altem Holz, dazu schicke ich Bilder mit. Mehr kann ich dann noch im Verlauf des Projektes schicken, da ich nur 10 Bilder auf einmal hochladen kann.
*Ich schicke Bilder aus einem Smoothie Rezept Buch, JPG 5465 das finde ich witzig um die Seite aufzulockern, vielleicht gibt es ja Ideen dazu wie es umgesetzt werden kann. - Dementsprechend möchte ich diese Elemente auch in dem Flyerprojekt im Anschluß umgesetzt haben.
Kräftige Farben sind gewünscht. Pink ist eh in meinem Logo. Gerne auch ein helles Lindgrün.

```html
<!DOCTYPE html>
<html lang="de">
<head>
<meta charset="utf-8">
<title>Rieke Solmberg – Outdoor Business Coaching</title>
<link href="https://fonts.googleapis.com/css2?family=Ubuntu:wght@500&family=Poppins:wght@300&display=swap" rel="stylesheet">
<style>
  :root {
    --page-bg: #f8f8f8;
    --nav-red: #e34c42;
    --nav-text: #ffffff;
    --lime: #bade58;
    --leaf: #a2c955;
    --olive: #c4c85a;
    --paper: #ffffff;
    --ink: #1e1e1e;
    --ink-soft: #555555;
  }
  * { margin: 0; padding: 0; box-sizing: border-box; }
  html, body { width: 1200px; height: 1200px; overflow: hidden; background: var(--page-bg); }
  .site {
    position: absolute; left: 68px; top: 302px; width: 1064px; height: 593px;
    background: var(--lime); overflow: hidden;
    box-shadow: -6px 8px 18px rgba(0,0,0,0.25);
  }
  .main-nav {
    position: absolute; left: 0; top: 0; width: 100%; height: 57px;
    background: var(--nav-red);
  }
  .main-nav a {
    position: absolute; top: 19px; color: var(--nav-text); text-decoration: none;
    font-family: "Ubuntu", sans-serif; font-weight: 500; font-size: 13.5px; white-space: nowrap;
  }
  .main-nav a.is-active::after {
    content: ""; position: absolute; left: 50px; width: 67px; top: 21px; height: 1px; background: var(--nav-text);
  }
  .menu-toggle { position: absolute; left: 1005px; top: 19px; width: 30px; height: 21px; }
  .menu-toggle span { display: block; height: 3px; background: var(--nav-text); margin-bottom: 6px; border-radius: 1px; }
  .hero { position: absolute; left: 0; top: 57px; width: 1064px; height: 536px; }
  .brand {
    position: absolute; left: 207px; top: 372px; width: 280px; text-align: center; color: var(--ink);
    white-space: nowrap;
  }
  .brand-name { font-family: "Poppins", sans-serif; font-weight: 300; font-size: 33px; line-height: 1; letter-spacing: -0.5px; }
  .brand-tagline { font-family: "Poppins", sans-serif; font-weight: 300; font-size: 10.5px; letter-spacing: 2.4px; color: var(--ink-soft); margin-top: 8px; }
</style>
</head>
<body>
<div class="site">
  <nav class="main-nav">
    <a class="is-active" style="left:85px">Bergabenteuer erleben!</a>
    <a style="left:268px">Gipfelglück genießen!</a>
    <a style="left:432px">Verzaubern lassen!</a>
    <a style="left:587px">Gemeinsam unterwegs sein!</a>
    <a style="left:796px">Deine Guide Rieke!</a>
    <div class="menu-toggle"><span></span><span></span><span></span></div>
  </nav>

  <svg class="hero" viewBox="0 0 1712 862" preserveAspectRatio="none">
    <defs>
      <linearGradient id="photo-boots" x1="0.7" y1="0" x2="0.2" y2="1">
        <stop offset="0" stop-color="#9cc0e6"/>
        <stop offset="0.12" stop-color="#b9b4ab"/>
        <stop offset="0.4" stop-color="#958c80"/>
        <stop offset="0.62" stop-color="#7a6f63"/>
        <stop offset="0.82" stop-color="#4e4a41"/>
        <stop offset="1" stop-color="#2f2d2a"/>
      </linearGradient>
      <linearGradient id="photo-summit" x1="0.2" y1="0" x2="0.4" y2="1">
        <stop offset="0" stop-color="#5e90d3"/>
        <stop offset="0.55" stop-color="#7eaadf"/>
        <stop offset="0.85" stop-color="#a3c6ea"/>
        <stop offset="0.94" stop-color="#c9b99c"/>
        <stop offset="1" stop-color="#a8967c"/>
      </linearGradient>
      <radialGradient id="summit-accent" cx="0.5" cy="0.6" r="0.35">
        <stop offset="0" stop-color="#e59bc8" stop-opacity="0.45"/>
        <stop offset="0.5" stop-color="#5fc8c4" stop-opacity="0.2"/>
        <stop offset="1" stop-color="#5fc8c4" stop-opacity="0"/>
      </radialGradient>
      <linearGradient id="photo-guide" x1="0" y1="0" x2="0.6" y2="1">
        <stop offset="0" stop-color="#a5a9ae"/>
        <stop offset="0.45" stop-color="#b9bdc2"/>
        <stop offset="0.7" stop-color="#6d6b68"/>
        <stop offset="0.86" stop-color="#2f312e"/>
        <stop offset="1" stop-color="#c2405a"/>
      </linearGradient>
      <radialGradient id="guide-accent" cx="0.72" cy="0.32" r="0.32">
        <stop offset="0" stop-color="#d9a07e" stop-opacity="0.75"/>
        <stop offset="0.55" stop-color="#8f7563" stop-opacity="0.35"/>
        <stop offset="1" stop-color="#8f7563" stop-opacity="0"/>
      </radialGradient>
      <filter id="lift" x="-10%" y="-10%" width="120%" height="120%">
        <feDropShadow dx="-4" dy="6" stdDeviation="6" flood-opacity="0.3"/>
      </filter>
    </defs>

    <rect class="field" width="1712" height="862" fill="var(--lime)"/>

    <path class="layer-leaf-right" fill="var(--leaf)" filter="url(#lift)"
      d="M960 0 C990 120 1100 150 1190 200 C1330 270 1440 330 1520 480 C1560 560 1540 700 1560 862 H1712 V0 Z"/>
    <path class="layer-olive-left" fill="var(--olive)" filter="url(#lift)"
      d="M0 0 H565 C560 150 470 270 380 300 C290 330 265 430 262 560 C258 710 150 830 0 862 Z"/>

    <path class="white-panel" fill="var(--paper)" filter="url(#lift)"
      d="M0 862 C110 850 150 780 210 720 C270 660 270 560 268 440 C266 350 300 310 380 295 C470 280 520 220 580 180 C640 140 720 150 790 148 C830 146 830 200 790 245 C760 280 770 300 815 292 C860 284 880 330 870 420 C860 520 840 640 760 720 C720 760 700 810 700 862 Z"/>

    <g role="img" aria-label="Foto: Wanderstiefel über einem Dolomitenpanorama">
      <path fill="url(#photo-boots)" filter="url(#lift)"
        d="M0 0 H485 C470 120 390 210 300 235 C225 258 215 380 205 520 C195 640 120 720 0 765 Z"/>
    </g>

    <path class="ring-olive-center" fill="var(--olive)" filter="url(#lift)"
      d="M900 260 C930 180 1010 150 1080 160 C1220 175 1360 230 1450 320 C1520 390 1530 520 1520 640 C1515 740 1530 800 1560 862 H740 C760 800 820 740 830 660 C840 560 860 360 900 260 Z"/>
    <g role="img" aria-label="Foto: zwei Wanderinnen jubeln mit ausgebreiteten Armen auf einem Gipfelfelsen">
      <path fill="url(#photo-summit)" filter="url(#lift)"
        d="M905 220 C960 170 1060 175 1160 195 C1290 220 1410 300 1470 400 C1510 480 1505 620 1480 720 C1465 790 1440 830 1420 862 H700 C660 790 700 730 780 690 C860 650 950 620 940 520 C930 420 850 290 905 220 Z"/>
      <path fill="url(#summit-accent)"
        d="M905 220 C960 170 1060 175 1160 195 C1290 220 1410 300 1470 400 C1510 480 1505 620 1480 720 C1465 790 1440 830 1420 862 H700 C660 790 700 730 780 690 C860 650 950 620 940 520 C930 420 850 290 905 220 Z"/>
    </g>

    <g role="img" aria-label="Foto: lächelnde Bergführerin mit Schirmmütze vor Felstürmen">
      <path fill="url(#photo-guide)" filter="url(#lift)"
        d="M1105 0 H1712 V720 C1640 725 1580 660 1550 560 C1520 460 1460 360 1380 290 C1300 220 1200 170 1150 110 C1120 75 1108 40 1105 0 Z"/>
      <path fill="url(#guide-accent)"
        d="M1105 0 H1712 V720 C1640 725 1580 660 1550 560 C1520 460 1460 360 1380 290 C1300 220 1200 170 1150 110 C1120 75 1108 40 1105 0 Z"/>
    </g>
  </svg>

  <div class="brand">
    <div class="brand-name">rieke solmberg</div>
    <div class="brand-tagline">outdoor business coaching</div>
  </div>
</div>
</body>
</html>
```